HVAC Door Hanger- 4.25 inches by 11 inches

Hello We are using the Brightwell door hanger as an inspiration for our new door hanger. The company name is Harborline Home Services. Logo files attached. The Slogan needs to be added on the front with the Logo "Southern California’s Trusted Name in Home Services". Instead of the X protection plan, the name will be Full Shield by Harborline or Harborline Climate Keeper- The slogan for this package will be "Peace of Mind, For Every Season

```html
<!DOCTYPE html>
<html lang="en">
<head>
<meta charset="utf-8">
<title>Harborline Home Services Door Hangers</title>
<link rel="stylesheet" href="https://fonts.googleapis.com/css2?family=Poppins:wght@400;500;600;700;800;900&display=swap">
<style>
:root{
  --blue:#1574ab;
  --orange:#f59d1c;
  --red:#e8222a;
  --dark-red:#b5121b;
  --ink:#333333;
  --cream:#fbf1e1;
  --cream-light:#fffaf2;
  --backdrop:#a3a3a3;
  --white:#ffffff;
}
*{margin:0;padding:0;box-sizing:border-box}
html,body{width:971px;height:1200px;overflow:hidden}
body{background:var(--backdrop);font-family:'Poppins',sans-serif;position:relative}
.hanger{position:absolute;top:104px;width:385px;height:994px;background:var(--white);overflow:hidden}
.hanger--front{left:84px}
.hanger--back{left:504px}
.hanger__hole{position:absolute;left:139px;top:47px;width:106px;height:106px;border-radius:50%;background:var(--backdrop)}
.hanger__art{position:absolute;left:0;top:0;width:385px;height:994px}
.line{position:absolute;left:0;width:100%;text-align:center;line-height:1;white-space:nowrap}

/* front */
.brand{position:absolute;left:33px;top:214px;width:310px}
.brand__name{font-size:40px;font-weight:800;color:var(--blue);letter-spacing:-0.5px;line-height:1}
.brand__sub{font-size:12px;font-weight:600;color:var(--orange);letter-spacing:10.5px;margin-top:2px}
.brand__trades{font-size:10.5px;font-weight:700;color:var(--red);letter-spacing:1.6px;margin-top:3px}
.slogan-top{top:512px;font-size:21px;font-weight:800;color:var(--ink);line-height:21px}
.headline-home{top:600px;font-size:94px;font-weight:900;color:var(--orange);letter-spacing:-2px}
.headline-services{top:676px;font-size:56px;font-weight:800;color:var(--blue);letter-spacing:-1px}
.dots{font-size:0;display:flex;justify-content:center;gap:4px;position:absolute;left:0;width:100%}
.dots i{display:block;width:5px;height:5px;border-radius:50%;background:var(--red)}
.question-1{top:762px;font-size:25px;font-weight:800;color:var(--ink)}
.question-2{top:792px;font-size:25px;font-weight:800;color:var(--blue)}
.reaction{position:absolute;top:830px;width:40px;height:40px;border-radius:50%;background:radial-gradient(circle at 40% 35%,#ffd84a,#f5a418)}

/* shared footer */
.call{position:absolute;left:43px;top:884px;width:298px;height:52px;border-radius:26px;background:linear-gradient(#f3333a,#d71820);display:flex;align-items:center;justify-content:center;gap:10px;box-shadow:0 8px 10px -6px rgba(0,0,0,.45)}
.call__icon{width:28px;height:28px;border-radius:50%;background:var(--white);display:flex;align-items:center;justify-content:center}
.call__number{font-size:31px;font-weight:800;color:var(--white);letter-spacing:0.5px}
.site{top:952px;font-size:16.5px;color:var(--white);letter-spacing:0.6px}
.site b{font-weight:700}

/* back */
.plan-name{top:355px;font-size:39px;font-weight:900;color:var(--red);letter-spacing:-0.5px}
.plan-sub{top:392px;font-size:22px;font-weight:800;color:var(--blue)}
.plan-sub span{color:var(--orange)}
.reduced{top:434px;font-size:11.5px;font-weight:600;color:#555}
.price{position:absolute;left:34px;top:457px;width:317px;height:30px;border-radius:15px;background:var(--orange);overflow:hidden;display:flex;align-items:center;font-weight:700;color:var(--white);font-size:13.5px}
.price__from{background:var(--red);height:100%;width:60px;display:flex;align-items:center;justify-content:center;border-radius:15px 0 0 15px}
.price__low{background:var(--blue);height:100%;width:125px;display:flex;align-items:center;justify-content:center;border-radius:15px 0 0 15px;margin-left:-6px}
.price__to{width:22px;height:22px;border-radius:50%;background:var(--red);display:flex;align-items:center;justify-content:center;font-size:11px;margin-left:-10px}
.price__high{flex:1;text-align:center}
.plans{position:absolute;left:28px;top:503px;width:328px;height:165px;border:1.3px solid var(--blue);border-radius:14px;background:var(--white)}
.plans__title{position:absolute;top:-10px;left:16px;right:16px;background:var(--white);text-align:center;font-size:15px;font-weight:800;color:var(--blue);line-height:20px;letter-spacing:-0.3px}
.plans__title span{color:var(--red)}
.plans__divider{position:absolute;left:164px;top:20px;width:1px;height:134px;background:var(--blue)}
.perk{position:absolute;display:flex;gap:6px;font-size:9.8px;line-height:12px;color:#555;font-weight:500}
.perk__icon{flex:none;width:22px;height:22px;border-radius:50%;display:flex;align-items:center;justify-content:center;border:2px solid #f0f0f0}
.perk__icon--red{background:var(--red)}
.perk__icon--blue{background:var(--blue)}
.perk__icon i{display:block;width:7px;height:7px;border-radius:50%;background:var(--white)}
.plans__more{position:absolute;left:184px;top:137px;font-size:10px;font-weight:700;color:var(--blue);letter-spacing:3px}
.offer-tag{position:absolute;left:28px;top:684px;width:71px;height:156px;background:var(--dark-red);border-radius:4px;text-align:center;color:var(--white)}
.offer-tag__reg{margin:8px auto 0;width:56px;height:52px;border:1px solid #f0b0b0;border-radius:3px;background:var(--red);font-weight:800;line-height:1}
.offer-tag__reg b{display:block;font-size:17px;padding-top:7px}
.offer-tag__reg span{display:block;font-size:18px;color:#ffcf4a;padding-top:2px}
.offer-tag__note{font-size:9.5px;font-weight:700;line-height:12px;margin-top:13px}
.offer-tag__note span{color:#ffcf4a}
.offer{position:absolute;left:103px;top:684px;width:254px;height:156px;background:var(--blue);border-radius:0 4px 4px 0;color:var(--white)}
.offer::before{content:"";position:absolute;left:-5px;top:4px;bottom:4px;border-left:3px dotted var(--white)}
.offer__kicker{position:absolute;left:19px;top:14px;font-size:13.5px;font-weight:800}
.offer__price{position:absolute;left:19px;top:29px;font-size:26px;font-weight:900;color:var(--orange);line-height:1}
.offer__rule{position:absolute;left:19px;right:36px;top:63px;height:1px;background:rgba(255,255,255,.6)}
.offer__system{position:absolute;left:19px;top:72px;font-size:10.5px;font-weight:700}
.offer__list{position:absolute;left:19px;top:88px;list-style:none;font-size:10.2px;line-height:16px}
.offer__list li{display:flex;align-items:center;gap:5px}
.offer__list li::before{content:"";width:5px;height:5px;border-radius:50%;background:var(--orange);border:1px solid var(--white)}
.limited{position:absolute;left:299px;top:669px;width:60px;height:60px;border-radius:50%;background:var(--red);border:2px solid var(--dark-red);color:var(--white);font-size:9px;font-weight:800;line-height:10px;text-align:center;display:flex;align-items:center;justify-content:center}
.limited span{color:#ffcf4a}
.peace{top:858px;left:-12px;font-size:13px;font-weight:700;color:#555}
.peace-mark{position:absolute;left:306px;top:853px;width:24px;height:24px;border-radius:50%;background:radial-gradient(circle at 40% 35%,#ffd84a,#f5a418)}
</style>
</head>
<body>

<!-- Front hanger -->
<div class="hanger hanger--front">
  <svg class="hanger__art" viewBox="0 0 385 994" aria-hidden="true">
    <defs>
      <linearGradient id="creamFront" x1="0" y1="0" x2="1" y2="1">
        <stop offset="0" stop-color="#fffaf2"/><stop offset="1" stop-color="#f8ead3"/>
      </linearGradient>
    </defs>
    <rect x="43" y="376" width="43" height="90" fill="#1574ab"/>
    <rect x="43" y="366" width="44" height="13" rx="6" fill="#f59d1c"/>
    <polygon points="0,590 192,353 385,590 385,903 0,903" fill="url(#creamFront)"/>
    <polygon points="0,530 192,296 385,530 385,590 192,353 0,590" fill="#1574ab"/>
    <rect x="0" y="903" width="385" height="91" fill="#1574ab"/>
    <polygon points="27,543 92,535 92,578 40,574 55,558" fill="#b5121b"/>
    <polygon points="358,543 293,535 293,578 345,574 330,558" fill="#b5121b"/>
    <path d="M65 552 Q192 588 321 552 L321 594 Q192 632 65 594 Z" fill="#e8222a"/>
    <path id="ribbonLine" d="M72 580 Q192 614 314 580" fill="none"/>
    <text font-family="Poppins, sans-serif" font-size="19" font-weight="600" fill="#fff" letter-spacing="2.5" text-anchor="middle">
      <textPath href="#ribbonLine" startOffset="50%">TRUSTED NAME IN</textPath>
    </text>
  </svg>
  <div class="hanger__hole"></div>

  <div class="brand">
    <div class="brand__name">HARBORLINE</div>
    <div class="brand__sub">HOME SERVICES</div>
    <div class="brand__trades">HEATING COOLING PLUMBING ELECTRICAL</div>
  </div>

  <div class="line slogan-top">SOUTHERN<br>CALIFORNIA’S</div>
  <div class="line headline-home">HOME</div>
  <div class="line headline-services">SERVICES</div>
  <div class="dots" style="top:741px"><i></i><i></i><i></i><i></i><i></i><i></i></div>
  <div class="line question-1">IS YOUR A/C</div>
  <div class="line question-2">SUMMER READY?</div>
  <div class="reaction" style="left:146px" role="img" aria-label="Surprised emoji"></div>
  <div class="reaction" style="left:199px" role="img" aria-label="Thinking emoji"></div>

  <div class="call">
    <span class="call__icon"><svg width="16" height="16" viewBox="0 0 24 24"><path d="M6.6 10.8a15 15 0 0 0 6.6 6.6l2.2-2.2c.3-.3.7-.4 1-.2 1.1.4 2.3.6 3.6.6.6 0 1 .4 1 1V20c0 .6-.4 1-1 1A17 17 0 0 1 3 4c0-.6.4-1 1-1h3.5c.6 0 1 .4 1 1 0 1.3.2 2.5.6 3.6.1.3 0 .7-.2 1z" fill="#1574ab"/></svg></span>
    <span class="call__number">555 0142 0199</span>
  </div>
  <div class="line site">www.<b>harborlinehomeservices</b>.com</div>
</div>

<!-- Back hanger -->
<div class="hanger hanger--back">
  <svg class="hanger__art" viewBox="0 0 385 994" aria-hidden="true">
    <defs>
      <linearGradient id="creamBack" x1="0" y1="0" x2="1" y2="1">
        <stop offset="0" stop-color="#fffaf2"/><stop offset="1" stop-color="#f8ead3"/>
      </linearGradient>
    </defs>
    <rect x="43" y="256" width="42" height="80" fill="#1574ab"/>
    <rect x="43" y="246" width="44" height="13" rx="6" fill="#f59d1c"/>
    <polygon points="0,470 192,233 385,470 385,903 0,903" fill="url(#creamBack)"/>
    <polygon points="0,410 192,176 385,366 385,430 192,233 0,470" fill="#1574ab"/>
    <rect x="0" y="903" width="385" height="91" fill="#1574ab"/>
  </svg>
  <div class="hanger__hole"></div>

  <div class="line plan-name">HARBORLINE</div>
  <div class="line plan-sub">CLIMATE <span>KEEPER</span></div>
  <div class="dots" style="top:423px"><i></i><i></i><i></i><i></i><i></i><i></i></div>
  <div class="line reduced">Monthly Service Reduced</div>

  <div class="price">
    <span class="price__from">From</span>
    <span class="price__low">$19.99/Month</span>
    <span class="price__to">to</span>
    <span class="price__high">$19.99/Month</span>
  </div>

  <div class="plans">
    <div class="plans__title">HARBORLINE HOME SERVICES <span>PLANS</span></div>
    <div class="plans__divider"></div>
    <div class="perk" style="left:14px;top:28px"><span class="perk__icon perk__icon--red"><i></i></span><span>One Harborline Home<br>Services Heating<br>Tune-up per year</span></div>
    <div class="perk" style="left:14px;top:76px"><span class="perk__icon perk__icon--blue"><i></i></span><span>One Harborline Home<br>Services A/C Tune-up<br>per year</span></div>
    <div class="perk" style="left:42px;top:131px"><span>10% Off In-Door<br>Air Quality Products</span></div>
    <div class="perk" style="left:180px;top:28px"><span class="perk__icon perk__icon--red"><i></i></span><span>One Water Heater<br>Flush per year</span></div>
    <div class="perk" style="left:180px;top:74px;align-items:center"><span class="perk__icon perk__icon--blue"><i></i></span><span>Priority Installation</span></div>
    <div class="perk" style="left:180px;top:106px;align-items:center"><span class="perk__icon perk__icon--red"><i></i></span><span>Transferrable Plan</span></div>
    <div class="plans__more">AND MUCH MORE</div>
  </div>

  <div class="offer-tag">
    <div class="offer-tag__reg"><b>REG.</b><span>$176</span></div>
    <div class="offer-tag__note">Get upto<br><span>$10,000</span><br>in state &amp;<br>federal<br>rebates!!!</div>
  </div>
  <div class="offer">
    <div class="offer__kicker">HALF OFF SPECIAL!</div>
    <div class="offer__price">ONLY $88</div>
    <div class="offer__rule"></div>
    <div class="offer__system">A/C System</div>
    <ul class="offer__list">
      <li>Safety inspection + Tune-Up</li>
      <li>Whole Home Water Safety Inspection</li>
      <li>Standard water heater flush</li>
      <li>Accessible drain cleaning</li>
    </ul>
  </div>
  <div class="limited"><div><span>LIMITED</span><br>TIME<br>OFFER</div></div>

  <div class="line peace">PEACE OF MIND, FOR EVERY SEASON</div>
  <div class="peace-mark" role="img" aria-label="Emoji with sunglasses"></div>

  <div class="call">
    <span class="call__icon"><svg width="16" height="16" viewBox="0 0 24 24"><path d="M6.6 10.8a15 15 0 0 0 6.6 6.6l2.2-2.2c.3-.3.7-.4 1-.2 1.1.4 2.3.6 3.6.6.6 0 1 .4 1 1V20c0 .6-.4 1-1 1A17 17 0 0 1 3 4c0-.6.4-1 1-1h3.5c.6 0 1 .4 1 1 0 1.3.2 2.5.6 3.6.1.3 0 .7-.2 1z" fill="#1574ab"/></svg></span>
    <span class="call__number">555 0142 0199</span>
  </div>
  <div class="line site">www.<b>harborlinehomeservices</b>.com</div>
</div>

</body>
</html>
```